Staff Newsletter Template Image

We are looking for two .jpg images that we can put into a Word document and use for our staff newsletter. We will then add content using text boxes.
Attached is the current template which works for the columns and size that we need but we just want a fresh new design.
The Word document shows how we use it.
The name will stay the same - Team upBeat but can be a different look to the current one.

Target Market(s)

Sales team

Colors

Designer to choose colors to be used in the design.

Requirements
Must have
• Colours will be green, grey and white, possibly cream if needed. All from the guidelines.
• I have attached our brand guidelines which shows design elements and fonts for our brand. Also attached is brand guidelines for one of our product lines as we would like to use the same green.
• It needs to be nice to look at and motivational for our team

```html
<!DOCTYPE html>
<html lang="en">
<head>
<meta charset="utf-8">
<title>Team upBeat – Staff Newsletter</title>
<link href="https://fonts.googleapis.com/css2?family=Nunito:ital,wght@0,400;0,600;0,700;1,700&display=swap" rel="stylesheet">
<style>
  :root {
    --green: #8cc63f;
    --green-light: #9acd55;
    --grey-bg: #e0e0df;
    --panel: #f0f0ef;
    --charcoal: #3a3a3a;
    --mid-grey: #939393;
    --text: #333333;
    --muted: #8f8f8f;
    --white: #ffffff;
  }
  * { margin: 0; padding: 0; box-sizing: border-box; }
  html, body { width: 1200px; height: 2659px; overflow: hidden; }
  body {
    background: var(--grey-bg);
    font-family: "Nunito", sans-serif;
    color: var(--text);
    position: relative;
  }
  .page {
    position: absolute;
    left: 173.5px;
    width: 854px;
    background: var(--white);
    box-shadow: 0 4px 14px rgba(0,0,0,0.18);
    overflow: hidden;
  }
  .page--one { top: 52px; height: 1208px; }
  .page--two { top: 1325px; height: 1207px; }
  .abs { position: absolute; }

  /* Header */
  .masthead { left: 0; top: 0; width: 854px; height: 268px; background: var(--green); }
  .masthead svg { position: absolute; left: 0; top: 0; }
  .brand-name {
    left: 48px; top: 92px;
    font-weight: 700; font-size: 64px; color: var(--white); letter-spacing: 0.5px;
  }
  .issue-date { right: 48px; font-weight: 700; font-size: 21px; color: var(--white); }
  .masthead .issue-date { top: 218px; }

  /* Intro */
  .greeting { left: 47px; top: 320px; font-weight: 700; font-size: 21px; }
  .placeholder { font-size: 16px; color: var(--muted); }
  .intro-text { left: 47px; top: 372px; }

  /* Right column panels */
  .panel { background: var(--panel); text-align: center; }
  .panel--sellers { left: 454.5px; top: 303px; width: 400px; height: 376px; }
  .panel--tip { left: 454.5px; top: 685px; width: 400px; height: 280px; }
  .panel--shout { left: 454.5px; top: 965px; width: 400px; height: 200px; background: var(--charcoal); color: var(--white); }
  .panel-title { font-weight: 700; font-size: 30px; line-height: 1.3; }
  .panel--sellers .panel-title { margin-top: 24px; }
  .panel-lede { font-size: 16.5px; line-height: 1.5; margin-top: 16px; }
  .panel-note { font-size: 16px; font-weight: 700; font-style: italic; margin-top: 14px; }

  .sellers-table {
    position: absolute; left: 19px; top: 196px; width: 361px;
    border-collapse: collapse; font-size: 16.5px; text-align: left;
  }
  .sellers-table th {
    background: var(--charcoal); color: var(--white); font-weight: 700;
    height: 37px; font-size: 16.5px;
  }
  .sellers-table th.rank-col { width: 41px; border-right: 1px solid #777; }
  .sellers-table th.member-col { padding-left: 30px; }
  .sellers-table td { height: 37px; border-bottom: 1px solid #d6d6d5; }
  .sellers-table tr:last-child td { border-bottom: none; }
  .sellers-table td.rank { font-weight: 700; text-align: center; border-right: 1px solid #d6d6d5; }
  .sellers-table td.prize { padding-left: 15px; }

  .panel--tip .panel-title { margin-top: 24px; }
  .panel--tip .placeholder { margin-top: 20px; }

  .panel--shout .panel-title { margin-top: 26px; }
  .shout-name { font-size: 21px; margin-top: 0px; }
  .shout-rule { width: 48px; height: 1px; background: #8a8a8a; margin: 9px auto 18px; }
  .panel--shout .placeholder { color: #e4e4e4; }

  /* Footer */
  .footer { left: 0; bottom: 0; width: 854px; height: 43px; background: var(--green); color: var(--white); }
  .footer .copyright { position: absolute; left: 48px; top: 10px; font-size: 18px; }
  .footer .issue-date { top: 10px; font-size: 19px; }

  /* Page two */
  .section { background: var(--panel); }
  .section--news { left: 0; top: 0; width: 398.5px; height: 578px; }
  .section--reminders { left: 0; top: 586px; width: 398.5px; height: 579px; }
  .section-head {
    position: absolute; left: 48px; top: 34px;
    font-weight: 700; font-size: 31px;
  }
  .section-head::before {
    content: ""; position: absolute; left: -28px; top: 15px;
    width: 12px; height: 12px; background: var(--green);
  }
  .section-head--grey::before { background: var(--mid-grey); }
  .section-body { position: absolute; left: 48px; top: 94px; }
  .tips { left: 420px; top: 0; width: 434px; height: 740px; }
  .tips .section-head { left: 48px; }
  .tips .section-body { left: 60px; }

  .values-strip { left: 409.5px; top: 743px; width: 444.5px; height: 13px; background: var(--mid-grey); }
  .panel--values { left: 409.5px; top: 756px; width: 444.5px; height: 409px; background: var(--charcoal); color: var(--white); text-align: center; }
  .panel--values .panel-title { margin-top: 46px; line-height: 1.3; }
  .panel--values .placeholder { color: #e4e4e4; margin-top: 14px; }
</style>
</head>
<body>

<section class="page page--one">
  <header class="masthead abs">
    <svg width="854" height="268" viewBox="0 0 854 268" aria-hidden="true">
      <path d="M0,195 C150,228 300,248 450,238 C600,228 740,192 854,198 L854,268 L0,268 Z" fill="var(--green-light)"/>
    </svg>
    <div class="brand-name abs">Brightwell</div>
    <div class="issue-date abs">02.07.2020</div>
  </header>

  <p class="greeting abs">Hi everyone,</p>
  <p class="intro-text placeholder abs">Place your text here...</p>

  <aside class="panel panel--sellers abs">
    <h2 class="panel-title">Top Sellers!</h2>
    <p class="panel-lede">The following upBeat team members<br>were our top sellers last week</p>
    <p class="panel-note">based on completed sales</p>
    <table class="sellers-table">
      <thead>
        <tr><th class="rank-col"></th><th class="member-col">Team Member</th></tr>
      </thead>
      <tbody>
        <tr><td class="rank">01</td><td class="prize">- 100 upBeat Dollars</td></tr>
        <tr><td class="rank">02</td><td class="prize">- 50 upBeat Dollars</td></tr>
        <tr><td class="rank">03</td><td class="prize">- 25 upBeat Dollars</td></tr>
      </tbody>
    </table>
  </aside>

  <aside class="panel panel--tip abs">
    <h2 class="panel-title">Top Tip from our<br>Week’s Top Seller</h2>
    <p class="placeholder">[Comments]</p>
  </aside>

  <aside class="panel panel--shout abs">
    <h2 class="panel-title">Shout Out</h2>
    <p class="shout-name">Name Here</p>
    <div class="shout-rule"></div>
    <p class="placeholder">[Comments]</p>
  </aside>

  <footer class="footer abs">
    <span class="copyright">© upBeat Massage Chairs</span>
    <span class="issue-date abs">02.07.2020</span>
  </footer>
</section>

<section class="page page--two">
  <div class="section section--news abs">
    <h2 class="section-head">Company News</h2>
    <p class="section-body placeholder">[News]</p>
  </div>

  <div class="section section--reminders abs">
    <h2 class="section-head">Reminders</h2>
    <p class="section-body placeholder">[Comments]</p>
  </div>

  <div class="tips abs">
    <h2 class="section-head section-head--grey">Tips &amp; Hints</h2>
    <p class="section-body placeholder">[Text]</p>
  </div>

  <div class="values-strip abs"></div>
  <aside class="panel panel--values abs">
    <h2 class="panel-title">Being an upBeat<br>Team Member Means...</h2>
    <p class="placeholder">[Text]</p>
  </aside>

  <footer class="footer abs">
    <span class="copyright">© upBeat Massage Chairs</span>
    <span class="issue-date abs">02.07.2020</span>
  </footer>
</section>

</body>
</html>
```